Yard sign design for high end luxury home builder.

Need a design for signage on custom homes that are being built. I already have a logo that I am satisfied with that needs to be incorporated. I need the following incorporated in the design of the sign-
- Lic number 318562
- phone number (555) 271-4038
- pendrickhomeworks.com
- Logo/Branding

If possible it may be nice to have the following quote that is on are business cards-

Quote from Osmund of Veltarra-
HE WHO WORKS WITH HIS HANDS IS A LABORER.
HE WHO WORKS WITH HIS HANDS & HIS HEAD IS A CRAFTSMAN.
HE WHO WORKS WITH HIS HANDS & HIS HEAD & HIS HEART IS AN ARTISAN.
-OSMUND OF VELTARRA

Target Market(s)

Archetect, Designers, Clients desiring to build a new home or remodel.

Colors
fde9d4
fee4d5
fabb94
fac994
faa54b
f68d4d
f37122
f78f20
f68e4e

Requirements
Must have
• - Lic number 318562
• - phone number (555) 271-4038
• - pendrickhomeworks.com
• - Logo/Branding
Nice to have
• Quote from Osmund of Veltarra-
• HE WHO WORKS WITH HIS HANDS IS A LABORER.
• HE WHO WORKS WITH HIS HANDS & HIS HEAD IS A CRAFTSMAN.
• HE WHO WORKS WITH HIS HANDS & HIS HEAD & HIS HEART IS AN ARTISAN.
• -OSMUND OF VELTARRA
• OR the below statement-
• Craftsmen that Care
Should not have
• Any additional verbiage not specified above including any type of verbiage about what kind of company we are. For instance- Integrity, reputable... It's just all played out. Im just looking for a bitching design that has the info that compliments my logo/branding.

```html
<!DOCTYPE html>
<html lang="en">
<head>
<meta charset="utf-8">
<title>Pendrick Homeworks Yard Sign</title>
<link rel="stylesheet" href="https://fonts.googleapis.com/css2?family=Montserrat:wght@500;600;700;800&family=Oswald:wght@500;600;700&display=swap">
<style>
  :root {
    --stage: #e6e4e1;
    --charcoal: #2e2e2e;
    --charcoal-dark: #222222;
    --ink: #111111;
    --paper: #ffffff;
    --orange: #f37122;
    --orange-soft: #f68d4d;
    --tan: #9a8268;
    --rule: #d8d8d8;
  }
  html, body {
    margin: 0;
    padding: 0;
    width: 1200px;
    height: 1200px;
    overflow: hidden;
    background: var(--stage);
  }
  .yard-sign {
    position: absolute;
    left: 180px;
    top: 40px;
    width: 840px;
    height: 1120px;
    background: radial-gradient(ellipse at 40% 30%, #3a3a3a 0%, var(--charcoal) 55%, var(--charcoal-dark) 100%);
    overflow: hidden;
    font-family: "Montserrat", sans-serif;
    color: var(--paper);
  }
  .brand {
    position: absolute;
    left: 0;
    right: 0;
    top: 200px;
    text-align: center;
    color: var(--tan);
    font-weight: 800;
    line-height: 1;
  }
  .brand-name { font-size: 78px; letter-spacing: 4px; }
  .brand-sub { font-size: 30px; letter-spacing: 3px; margin-top: 18px; }
  .quote-rule {
    position: absolute;
    left: 0;
    right: 0;
    display: flex;
    justify-content: center;
    align-items: center;
    gap: 28px;
  }
  .quote-rule .line { width: 156px; height: 2px; background: var(--rule); }
  .quote-rule .mark { font-size: 30px; font-weight: 700; width: 20px; text-align: center; line-height: 1; }
  .quote-rule.open { top: 450px; }
  .quote-rule.close { top: 668px; }
  .quote-text {
    position: absolute;
    left: 40px;
    right: 40px;
    top: 500px;
    text-align: center;
    font-weight: 600;
    font-size: 22px;
    line-height: 28px;
    letter-spacing: 0.3px;
  }
  .quote-text p { margin: 0 0 19px; }
  .attribution {
    position: absolute;
    right: 100px;
    top: 710px;
    font-size: 22px;
    font-weight: 700;
    letter-spacing: 0.5px;
  }
  .contact-panel { position: absolute; left: 0; top: 0; }
  .contact-heading {
    position: absolute;
    left: 0;
    right: 0;
    top: 840px;
    text-align: center;
    font-family: "Oswald", sans-serif;
    font-weight: 700;
    font-size: 56px;
    line-height: 1;
    color: var(--ink);
  }
  .contact-phone {
    position: absolute;
    left: 0;
    right: 0;
    top: 890px;
    text-align: center;
    font-family: "Oswald", sans-serif;
    font-weight: 600;
    font-size: 90px;
    line-height: 1;
    color: var(--orange);
  }
  .license {
    position: absolute;
    left: 50%;
    top: 1017px;
    transform: translateX(-50%);
    height: 34px;
    padding: 0 18px;
    border-radius: 17px;
    background: var(--ink);
    display: flex;
    align-items: center;
    gap: 8px;
    font-family: "Oswald", sans-serif;
    font-weight: 500;
    font-size: 20px;
    white-space: nowrap;
  }
  .license .label { color: var(--paper); }
  .license .number { color: var(--orange-soft); }
  .website {
    position: absolute;
    left: 0;
    right: 0;
    top: 1074px;
    text-align: center;
    font-size: 18px;
    font-weight: 500;
    letter-spacing: 6px;
    color: #333333;
  }
</style>
</head>
<body>
  <main class="yard-sign">
    <div class="brand">
      <div class="brand-name">PENDRICK</div>
      <div class="brand-sub">HOMEWORKS INC.</div>
    </div>

    <div class="quote-rule open"><span class="line"></span><span class="mark">&ldquo;</span><span class="line"></span></div>
    <div class="quote-text">
      <p>HE WHO WORKS WITH HIS HANDS IS A LABORER.</p>
      <p>HE WHO WORKS WITH HIS HANDS AND HEAD IS A CRAFTSMAN</p>
      <p>HE WHO WORKS WITH HIS HANDS AND HEAD AND HIS<br>HEART IS AN ARTISAN.</p>
    </div>
    <div class="quote-rule close"><span class="line"></span><span class="mark">&rdquo;</span><span class="line"></span></div>
    <div class="attribution">- OSMUND OF VELTARRA</div>

    <svg class="contact-panel" width="840" height="1120" viewBox="0 0 840 1120" aria-hidden="true">
      <polygon points="0,880 406,744 840,880 840,1120 0,1120" fill="var(--orange)"/>
      <polygon points="0,893 406,758 840,893 840,1120 0,1120" fill="var(--paper)"/>
    </svg>
    <div class="contact-heading">CONTACT US</div>
    <div class="contact-phone">(555) 271-4038</div>
    <div class="license"><span class="label">LIC NUMBER</span><span class="number">318562</span></div>
    <div class="website">PENDRICKHOMEWORKS.COM</div>
  </main>
</body>
</html>
```